Fern and Slate Mobile Bartending Website

Looking for an informational website for our mobile bartending business. We want to include features we like from another website that will help support our business.

Something with a similar set-up to https://velvetfinchpours.com/

```html
<!DOCTYPE html>
<html lang="en">
<head>
<meta charset="utf-8">
<title>Fern and Slate Mobile Bartending</title>
<link rel="stylesheet" href="https://fonts.googleapis.com/css2?family=Libre+Baskerville&family=Poppins:wght@400;500;600&display=swap">
<style>
:root{
  --rose:#c49a98;
  --rose-dark:#b0827f;
  --cream:#f3e9e0;
  --blush:#f6efee;
  --ivory:#f5f1ea;
  --ink:#2a2a2a;
  --text:#444;
  --muted:#777;
  --footer:#2b2b2b;
  --footer-deep:#1f1f1f;
  --white:#fff;
}
*{box-sizing:border-box;margin:0;padding:0}
html,body{width:1200px;height:4869px;overflow:hidden}
body{font-family:"Poppins",sans-serif;color:var(--text);background:var(--white);position:relative}
.serif{font-family:"Libre Baskerville",serif;text-transform:uppercase;color:var(--ink);font-weight:400}
section,header,footer{position:absolute;left:0;width:1200px}
.abs{position:absolute}
.btn{position:absolute;background:var(--rose);color:var(--white);font-size:9px;font-weight:600;letter-spacing:1.5px;text-transform:uppercase;display:flex;align-items:center;justify-content:center}
.body-copy{font-size:12px;line-height:24.5px;color:var(--text)}

/* header */
.topbar{top:0;height:53px;background:var(--cream)}
.topbar .util{position:absolute;top:14px;display:flex;align-items:center;gap:14px;font-size:10px;color:var(--ink);text-transform:uppercase}
.util .dot{width:24px;height:24px;border-radius:50%;background:var(--rose)}
.follow{position:absolute;right:134px;top:15px;display:flex;align-items:center;gap:8px;font-size:10px;font-weight:600;color:var(--ink)}
.follow span.c{width:22px;height:22px;border-radius:50%;background:var(--rose)}
.nav{top:53px;height:64px;background:var(--white)}
.nav a{position:absolute;top:25px;font-size:10.5px;color:var(--ink);text-decoration:none;text-transform:uppercase}
.brand-box{position:absolute;left:499px;top:0;width:202px;height:110px;background:var(--white);box-shadow:0 2px 10px rgba(0,0,0,.08);z-index:2;display:flex;flex-direction:column;align-items:center;justify-content:center;gap:4px}
.brand-box .name{font-family:"Poppins",sans-serif;font-size:22px;font-weight:500;color:var(--ink);letter-spacing:.5px}
.brand-box .sq{width:16px;height:16px;background:var(--ink)}

/* hero */
.hero{top:117px;height:673px;background:linear-gradient(90deg,#f4f2f1 0%,#eeeaea 40%,#d9b7b8 65%,#a8424e 85%,#8a2f3b 100%)}
.hero h1{position:absolute;left:134px;top:195px;width:560px;font-size:41px;line-height:48px}
.hero p{position:absolute;left:134px;top:340px;width:460px;font-size:11px;line-height:23px}

/* about */
.about{top:790px;height:794px}
.about .portrait{position:absolute;left:111px;top:193px;width:500px;height:500px;border-radius:50%;background:linear-gradient(180deg,#f3f0e9,#e3ddd3)}
.about h2{position:absolute;left:652px;top:208px;font-size:40px}
.about .body-copy{position:absolute;left:652px;width:412px}

/* services */
.services{top:1584px;height:731px;background:var(--blush)}
.services h2{position:absolute;left:0;width:1200px;text-align:center;top:90px;font-size:40px}
.card{position:absolute;width:295px;height:372px;display:flex;align-items:flex-end;justify-content:center;padding-bottom:38px}
.card span{position:relative;font-family:"Libre Baskerville",serif;color:var(--white);font-size:15.5px;text-transform:uppercase}
.num{position:absolute;font-family:"Libre Baskerville",serif;font-size:100px;color:var(--rose);line-height:1;letter-spacing:-6px}

/* testimonials */
.testimonials{top:2315px;height:535px}
.testimonials h2{position:absolute;left:134px;top:90px;font-size:40px;line-height:48px}
.arrow{position:absolute;width:52px;height:52px;border-radius:50%;display:flex;align-items:center;justify-content:center}
.quote{position:absolute;top:236px;width:382px;height:201px;background:var(--white);box-shadow:0 4px 18px rgba(0,0,0,.09);padding:28px 30px}
.quote .marks{font-family:"Libre Baskerville",serif;color:var(--rose);font-size:44px;line-height:30px;height:34px}
.quote p{font-size:11px;line-height:21px;color:var(--text);width:330px}
.quote .who{position:absolute;right:30px;bottom:26px;text-align:left;font-size:10px;line-height:18px}
.quote .who b{color:var(--rose);font-weight:500;text-transform:uppercase;display:block}
.avatar{position:absolute;top:261px;width:52px;height:52px;border-radius:50%;background:linear-gradient(135deg,#d9d0c6,#8e8a86)}

/* request */
.request{top:2850px;height:429px;background:var(--ivory)}
.request h2{position:absolute;left:0;width:1200px;text-align:center;top:87px;font-size:40px;line-height:48px}
.request p{position:absolute;left:208px;width:784px;top:193px;text-align:center;font-size:11px;line-height:25px}

/* featured */
.featured{top:3279px;height:350px}
.featured h2{position:absolute;left:0;width:1200px;text-align:center;top:93px;font-size:40px}
.press{position:absolute;top:189px;width:216px;height:117px;background:var(--white);box-shadow:0 4px 16px rgba(0,0,0,.08);display:flex;align-items:center;justify-content:center;font-size:15px;font-weight:600;color:var(--ink)}

/* follow */
.follow-us{top:3629px;height:680px}
.follow-us h2{position:absolute;left:0;width:1200px;text-align:center;top:50px;font-size:40px}
.polaroid{position:absolute;width:266px;height:300px;background:var(--white);box-shadow:0 6px 18px rgba(0,0,0,.12);padding:16px 16px 50px}
.polaroid div{width:100%;height:100%}

/* footer */
.site-footer{top:4309px;height:501px;background:var(--footer);color:#d8d8d8}
.site-footer .fname{position:absolute;left:132px;top:150px;font-size:28px;font-weight:500;color:var(--white)}
.site-footer .fsq{position:absolute;left:214px;top:108px;width:30px;height:30px;background:var(--white)}
.site-footer .fcopy{position:absolute;left:132px;top:222px;width:275px;font-size:10.5px;line-height:26px;color:#e0e0e0}
.site-footer h3{position:absolute;font-family:"Libre Baskerville",serif;font-weight:400;font-size:16px;text-transform:uppercase;color:var(--white)}
.site-footer .link{position:absolute;left:471px;font-size:12px;color:#e6e6e6}
.site-footer .soc{position:absolute;top:4377px;width:30px;height:30px;border-radius:50%;background:var(--rose)}
.contact{position:absolute;left:790px;top:118px;width:302px;height:288px;background:var(--rose)}
.contact .row{position:absolute;left:42px;display:flex;gap:18px;align-items:flex-start}
.contact .row small{display:block;font-size:6.5px;letter-spacing:.5px;text-transform:uppercase;color:var(--white)}
.contact .row span{font-size:9.5px;line-height:20px;color:var(--white)}
.copyright{top:4810px;height:59px;background:var(--footer-deep);color:#e6e6e6;font-size:11.5px;display:flex;align-items:center;justify-content:center}
</style>
</head>
<body>

<header class="topbar">
  <div class="util" style="left:134px"><span class="dot"></span>Account</div>
  <div class="util" style="left:262px"><span class="dot"></span>Cart (0)</div>
  <div class="follow">FOLLOW US ON: <span class="c" aria-label="Social link"></span><span class="c" aria-label="Social link"></span><span class="c" aria-label="Social link"></span></div>
</header>
<nav class="nav" style="position:absolute;left:0;width:1200px">
  <a style="left:134px">About Us</a>
  <a style="left:242px">FAQs</a>
  <a style="left:322px">Packages + Bars</a>
  <a style="left:779px">Cocktail Menu</a>
  <a style="left:930px">Alcohol Calculator</a>
</nav>
<div class="brand-box"><span class="sq"></span><span class="name">FERN &amp; SLATE</span></div>

<section class="hero" role="img" aria-label="Row of red cocktails in stemmed glasses on a bright bar">
  <h1 class="serif">Shake it up with the best bartenders in town.</h1>
  <p>Lorem Ipsum is simply dummy text of the printing and typesetting industry. Lorem Ipsum has been the industry's standard dummy text ever since the 1500s, when an unknown printer took a galley of type and scrambled.</p>
  <div class="btn" style="left:134px;top:442px;width:231px;height:35px">Schedule Consultation</div>
</section>

<section class="about">
  <div class="portrait" role="img" aria-label="Bartender in an apron holding a blue cocktail and a shaker"></div>
  <h2 class="serif">About Us</h2>
  <p class="body-copy" style="top:262px">Lorem Ipsum is simply dummy text of the printing and typesetting industry. Lorem Ipsum has been the industry's standard dummy text ever since the 1500s, when an unknown printer took a galley of type and scrambled it to make a type specimen book. It has survived not only five centuries.</p>
  <p class="body-copy" style="top:410px">but also the leap into electronic typesetting, remaining essentially unchanged. It was popularised in the 1960s with the release of Letraset sheets containing Lorem Ipsum passages, and more recently with desktop publishing software like Aldus PageMaker including versions of Lorem Ipsum.</p>
  <div class="btn" style="left:652px;top:571px;width:223px;height:38px">Read More</div>
</section>

<section class="services">
  <h2 class="serif">Unique Bartending Services</h2>
  <div class="card" style="left:134px;top:193px;background:linear-gradient(180deg,#2f2a26,#7a4a22 60%,#1c1512)" role="img" aria-label="Bartender garnishing an orange cocktail"><span>Packages + Bars</span></div>
  <div class="num" style="left:228px;top:552px">01</div>
  <div class="num" style="left:546px;top:183px">02</div>
  <div class="card" style="left:452px;top:259px;background:linear-gradient(180deg,#0d0d0d,#c87a1c 50%,#1a1a1a)" role="img" aria-label="Three colourful cocktails with fruit garnish"><span>Cocktail Menu</span></div>
  <div class="card" style="left:769px;top:193px;background:linear-gradient(180deg,#1d2a4a,#5a2f6e 50%,#7a2a22)" role="img" aria-label="Layered shots being poured at a bar"><span>Alcohol Calculator</span></div>
  <div class="num" style="left:864px;top:552px">03</div>
</section>

<section class="testimonials">
  <h2 class="serif">What our client<br>says</h2>
  <div class="arrow" style="left:945px;top:111px;background:#e6c9c3">
    <svg width="16" height="16" viewBox="0 0 16 16"><path d="M10 3 5 8l5 5" fill="none" stroke="#fff" stroke-width="2.2"/></svg></div>
  <div class="arrow" style="left:1013px;top:111px;background:var(--rose)">
    <svg width="16" height="16" viewBox="0 0 16 16"><path d="m6 3 5 5-5 5" fill="none" stroke="#fff" stroke-width="2.2"/></svg></div>
  <div class="avatar" style="left:127px" role="img" aria-label="Client portrait"></div>
  <div class="quote" style="left:195px">
    <div class="marks">&ldquo;</div>
    <p>Lorem Ipsum is simply dummy text of the printing and typesetting industry. Lorem Ipsum has been the industry's standard dummy text ever</p>
    <div class="who"><b>Mara Lindqvist</b>Manager</div>
  </div>
  <div class="avatar" style="left:622px" role="img" aria-label="Client portrait"></div>
  <div class="quote" style="left:690px">
    <div class="marks">&ldquo;</div>
    <p>Lorem Ipsum is simply dummy text of the printing and typesetting industry. Lorem Ipsum has been the industry's standard dummy text ever</p>
    <div class="who"><b>Mara Lindqvist</b>Manager</div>
  </div>
</section>

<section class="request">
  <h2 class="serif">Request our services for<br>your next event!</h2>
  <p>Lorem Ipsum is simply dummy text of the printing and typesetting industry. Lorem Ipsum has been the industry's standard dummy text ever since the 1500s, when an unknown printer took a galley of type and scrambled it to make a type specimen book. It has survived not only five centuries.</p>
  <div class="btn" style="left:486px;top:297px;width:228px;height:36px">Schedule Consultation</div>
</section>

<section class="featured">
  <h2 class="serif">We're featured in</h2>
  <svg class="abs" style="left:44px;top:240px" width="80" height="30" viewBox="0 0 80 30"><circle cx="25" cy="15" r="15" fill="#f2ece6"/><path d="M76 15H20M28 9l-8 6 8 6" fill="none" stroke="#222" stroke-width="2"/></svg>
  <div class="press" style="left:134px">Meridian Wire</div>
  <div class="press" style="left:373px">Fieldline Sports</div>
  <div class="press" style="left:611px">Harbor Channel</div>
  <div class="press" style="left:851px">Skyline Report</div>
  <svg class="abs" style="left:1076px;top:237px" width="84" height="36" viewBox="0 0 84 36"><circle cx="54" cy="18" r="18" fill="var(--rose)"/><path d="M4 18h56M52 12l8 6-8 6" fill="none" stroke="#222" stroke-width="2"/></svg>
</section>

<section class="follow-us">
  <h2 class="serif">Follow us on</h2>
  <div class="polaroid" style="left:78px;top:165px;transform:rotate(-3deg)"><div role="img" aria-label="Guests celebrating with sparklers" style="background:linear-gradient(135deg,#3a2a20,#c89a4a 50%,#2a1e18)"></div></div>
  <div class="polaroid" style="left:352px;top:140px;transform:rotate(3deg)"><div role="img" aria-label="Row of red cocktails on a bar" style="background:linear-gradient(135deg,#5a1a24,#d44a5a 50%,#2a1218)"></div></div>
  <div class="polaroid" style="left:620px;top:150px;transform:rotate(-8deg)"><div role="img" aria-label="Bartender straining a yellow cocktail" style="background:linear-gradient(135deg,#d8d8d8,#e8b04a 50%,#1a1a1a)"></div></div>
  <div class="polaroid" style="left:860px;top:150px;transform:rotate(8deg)"><div role="img" aria-label="Bartender pouring a drink" style="background:linear-gradient(135deg,#3a3030,#8a2a2a 50%,#1a1414)"></div></div>
  <div class="btn" style="left:488px;top:544px;width:224px;height:36px">Visit Our Instagram</div>
</section>

<footer class="site-footer">
  <span class="fsq"></span>
  <div class="fname">FERN &amp; SLATE</div>
  <p class="fcopy">Lorem Ipsum is simply dummy text of the printing and typesetting industry. Lorem Ipsum has been the industry's standard dummy text ever since the 1500s, when an unknown printer took a galley of type and scrambled it to make a type specimen book.</p>
  <h3 style="left:471px;top:120px">Quick Links</h3>
  <div class="link" style="top:185px">Packages + Bars</div>
  <div class="link" style="top:230px">Alcohol Calculator</div>
  <div class="link" style="top:274px">Cocktail Menu</div>
  <div class="link" style="top:317px">About Us</div>
  <span class="soc" style="left:473px;top:375px" aria-label="Social link"></span>
  <span class="soc" style="left:528px;top:375px" aria-label="Social link"></span>
  <span class="soc" style="left:582px;top:375px" aria-label="Social link"></span>
  <div class="contact">
    <h3 style="left:42px;top:40px">Contact</h3>
    <div class="row" style="top:88px">
      <svg width="18" height="14" viewBox="0 0 18 14"><rect x="1" y="1" width="16" height="12" fill="#fff"/><path d="m1 1 8 7 8-7" fill="none" stroke="var(--rose)" stroke-width="1.5"/></svg>
      <div><small>Mail</small><span>info@fernslatebar.com</span></div>
    </div>
    <div class="row" style="top:148px">
      <svg width="18" height="18" viewBox="0 0 18 18"><path d="M17 1 1 8l7 2 2 7z" fill="#fff"/></svg>
      <div><small>Address</small><span>Fern &amp; Slate LLC 418 Larkspur Ave<br>Ste 12 Millbrook, KS 67010</span></div>
    </div>
    <div class="row" style="top:222px">
      <svg width="18" height="18" viewBox="0 0 18 18"><path d="M4 1l3 4-2 2c1 3 3 5 6 6l2-2 4 3-2 3C8 17 1 10 1 3z" fill="#fff"/></svg>
      <div><small>Phone</small><span>(555) 014-2290</span></div>
    </div>
  </div>
</footer>

<div class="copyright" style="position:absolute;left:0;width:1200px">&copy; 2023 FERN &amp; SLATE LLC. ALL RIGHTS RESERVED.</div>

</body>
</html>
```